Croatia Luxury Cruise Brochure

1) Front page instead of By Orchard Path with Liesl please put by Pinecrest Harbor Guild – same on the last page where you have her contacts
2) Can you please add into the second page where you have ‘Welcome to your Croatia trip’ itinerary at glance. You can put it just below the text you have. Create a nice looking table .
D1 August 05, 2023 Arrival to Dubrovnik , Welcome cocktail party on Dubrovnik city walls
D2 August 06, 2023 Dubrovnik Highlights city tour – Embark sail to Elafiti
D3 August 07, 2023 Sail to Mljet island and day at leisure at sea
D4 August 08, 2023 Peljesac Wine Tasting with Live Music – Sail to Korcula
D5 August 09, 2023 Korcula Highlights Explorer Tour & Local Estate Dinner
D6 August 10, 2023 Korcula to Vis Island sail
D7 August 11, 2023 Vis Militarty Tour -sail to Pakleni Islands Bortelli sunset cocktails
D8 August 12, 2023 Hvar island – sail to Split
D9 August 13, 2023 Disembark – Split & Trogir ORVALD tours with 6-course wine dinner
D10 August 14, 2023 Fly out
Note: All tours & Experiences are optional add ons except the Cocktail reception on Dubrovnik city walls
3) Changes to the itinerary:
D1 is now arrival to Dubrovnik day earlier (AUGU5) and the rest is all moved accordingly. Please check the link
https://portal.kelvoro-desk. com/itinerary/custom-trip-prepared-for-liesl-group/
4) Inclusion/Exclusion page we need to update a little. Please make 3 different categories with a note for booking conditions.
Inclusions
• All transfers per itinerary including airport pick up and drop off
• 7 nights cruise on MS Dovetail on half board basis
• All meals stated per itinerary
• Captains dinner
• Unlimited water
• Masseuse on board
• Service of 11 crew members
• Cruise director
• Unlimited WiFi
• Daily cleaning
• Arrival refreshments
• Premium docking
• Usage of non motorized water toys
• Exclusive cocktail reception on Dubrovnik city walls with live music and snacks
Optional Tours
• Dubrovnik Highlights Explorer tour
• Peljesac Wine tour with live music
• Korcula explorer tour with local estate dinner
• Vis Military tour
• Bortelli Lounge bar reservation (min spend EUR100 per person)
• Split & Trogir ORVALD Explorer tour
• 6-course farewell dinner with local wine pairing
• 1 night post stay in Velmont 5* hotel in Split (This is added on optional)
Extras
• Tips for the crew
• Beverage consumption
• Usage of motorized water toys – EUR150 per hour
• International flights
• Any personal expenses
Booking conditions
30 % non-refundable deposit needed upon confirmation
Balance of the trip and any optional tours picked are due 06 May, 2023
Luxury travelers from USA and Canada
Tourism

```html
<!DOCTYPE html>
<html lang="en">
<head>
<meta charset="utf-8">
<title>Croatia Luxury Explorer Cruise Brochure</title>
<link rel="stylesheet" href="https://fonts.googleapis.com/css2?family=Fira+Sans+Condensed:wght@400;500;600;700&family=Montserrat:wght@300;400&display=swap">
<style>
  :root{
    --bg:#e5e6e8;
    --gap:#ffffff;
    --blue:#1b86d6;
    --blue-dark:#1565b0;
    --blue-light:#4fb3f0;
    --navy:#0b2a55;
    --sky:#e6f3fb;
    --paper:#ffffff;
    --ink:#3b3b3b;
    --muted:#7c8590;
    --disc:#4a4a4c;
  }
  *{box-sizing:border-box;margin:0;padding:0}
  html,body{width:1200px;height:2660px;overflow:hidden;background:var(--gap)}
  body{font-family:"Fira Sans Condensed",sans-serif;color:var(--ink)}
  .stage{position:absolute;left:0;width:1200px;height:660px;background:var(--bg)}
  .stage--covers{top:0}
  .stage--cover-solo{top:665px}
  .stage--spread-intro{top:1330px}
  .stage--spread-days{top:1995px}

  .spread{position:absolute;left:160px;top:160px;width:880px;height:340px;display:flex;box-shadow:0 14px 30px rgba(0,0,0,.18)}
  .page{position:relative;width:440px;height:340px;background:var(--paper);overflow:hidden}
  .page svg.art{position:absolute;inset:0;width:100%;height:100%}
  .page--left{box-shadow:inset -10px 0 14px -10px rgba(0,0,0,.25)}
  .page--right{box-shadow:inset 10px 0 14px -10px rgba(0,0,0,.2)}

  /* front cover */
  .cover-title{position:absolute;right:40px;top:40px;font-family:"Montserrat",sans-serif;font-weight:300;font-size:36px;letter-spacing:3px;color:var(--blue-dark)}
  .cover-tagline{position:absolute;right:22px;top:190px;text-align:right;font-size:14px;line-height:1.1;color:#fff;text-transform:uppercase}
  .cover-dates{position:absolute;left:24px;bottom:48px;font-size:11px;line-height:1.25;color:#fff;text-transform:uppercase}
  .cover-credit{position:absolute;right:22px;bottom:24px;font-size:9px;font-weight:500;letter-spacing:1px;color:#fff;text-transform:uppercase}
  .site{position:absolute;font-size:7px;letter-spacing:3px;color:#fff;font-weight:600;text-transform:uppercase}
  .cover-site{left:24px;bottom:26px}

  .stage--cover-solo .cover{position:absolute;left:610px;top:121px;width:540px;height:418px;box-shadow:0 16px 34px rgba(0,0,0,.2)}
  .stage--cover-solo .cover .page{width:540px;height:418px}
  .stage--cover-solo .cover-title{font-size:44px;right:46px;top:46px}
  .stage--cover-solo .cover-tagline{font-size:17px;right:28px;top:236px}
  .stage--cover-solo .cover-dates{font-size:13px;left:30px;bottom:58px}
  .stage--cover-solo .cover-site{font-size:8.5px;left:30px;bottom:32px}
  .stage--cover-solo .cover-credit{font-size:10px;right:28px;bottom:30px}

  /* inclusions page */
  .inclusions-page{position:absolute;left:50px;top:121px;width:540px;height:418px;box-shadow:0 16px 34px rgba(0,0,0,.16)}
  .inclusions-page .page{width:540px;height:418px;padding:22px 24px 0}
  .inclusions-page .section-title{font-size:18px;margin-bottom:12px}
  .terms{display:grid;grid-template-columns:1.15fr 1fr .85fr;gap:16px}
  .terms h3{font-size:10px;font-weight:700;color:#fff;background:var(--blue);text-transform:uppercase;letter-spacing:.5px;padding:3px 7px;margin-bottom:6px}
  .terms ul{list-style:none}
  .terms li{position:relative;padding-left:9px;font-size:7.6px;line-height:1.32;color:#555;margin-bottom:2.5px}
  .terms li::before{content:"";position:absolute;left:0;top:3.5px;width:4px;height:4px;border-radius:50%;background:var(--blue)}
  .booking{position:absolute;left:24px;right:24px;bottom:42px;background:var(--sky);border-left:3px solid var(--blue);padding:7px 10px}
  .booking h3{font-size:10px;font-weight:700;color:var(--blue);text-transform:uppercase;margin-bottom:3px}
  .booking p{font-size:7.8px;line-height:1.4;color:#444}
  .inclusions-page .folio-line{left:24px;right:24px;width:auto}
  .inclusions-page .footer-site{left:24px;bottom:26px}

  /* back cover */
  .contact{position:absolute;left:34px;top:132px;width:170px;font-size:8px;line-height:1.55;color:var(--muted)}
  .contact h2{font-size:12px;font-weight:700;color:var(--blue);letter-spacing:.5px;margin-bottom:2px}
  .contact .agency{font-size:9px;font-weight:600;color:var(--navy);margin-bottom:3px}
  .contact li{list-style:none;display:flex;align-items:flex-start;gap:5px}
  .contact svg{width:8px;height:8px;fill:var(--blue);margin-top:3px;flex:none}
  .back-site{left:150px;bottom:22px}

  /* footers */
  .folio{position:absolute;bottom:14px;width:16px;height:16px;border-radius:50%;background:var(--blue);color:#fff;font-size:9px;font-weight:600;display:flex;align-items:center;justify-content:center}
  .folio-line{position:absolute;bottom:21px;height:1px;background:var(--blue)}
  .page--left .folio{left:20px}
  .page--left .folio-line{left:36px;width:250px}
  .page--left .footer-site{right:24px;bottom:17px}
  .page--right .folio{right:20px}
  .page--right .folio-line{right:36px;width:250px}
  .page--right .footer-site{left:20px;bottom:17px}
  .footer-site.on-light{color:var(--blue)}

  /* itinerary at a glance */
  .itinerary{position:absolute;left:22px;top:24px;width:396px;background:rgba(8,32,70,.84);border-top:3px solid var(--blue);padding:10px 14px 9px}
  .itinerary h2{font-size:14px;font-weight:700;color:#fff;text-transform:uppercase;letter-spacing:.5px;margin-bottom:5px}
  .itinerary table{width:100%;border-collapse:collapse}
  .itinerary th{font-size:7.2px;font-weight:600;color:var(--blue-light);text-transform:uppercase;text-align:left;letter-spacing:.5px;padding:2px 4px;border-bottom:1px solid var(--blue)}
  .itinerary td{font-size:7.4px;color:#fff;padding:3px 4px;line-height:1.2;white-space:nowrap}
  .itinerary tr:nth-child(even) td{background:rgba(255,255,255,.07)}
  .itinerary td.day{color:var(--blue-light);font-weight:700;width:26px}
  .itinerary td.date{width:74px;color:#cfe9f8}
  .itinerary .note{font-size:6.8px;color:#cfe9f8;margin-top:5px}

  /* about */
  .about{position:absolute;left:226px;top:70px;width:188px}
  .section-title{font-weight:700;color:var(--blue);text-transform:uppercase;line-height:1.05}
  .about .section-title{font-size:17px;margin-bottom:6px}
  .body-copy{font-size:7.2px;line-height:1.45;color:#555;text-align:justify}
  .body-copy + .body-copy{margin-top:6px}

  /* day pages */
  .day-tag{position:absolute;background:var(--blue);color:#fff;font-weight:700;font-size:14px;display:flex;align-items:center;justify-content:center}
  .day-tag--one{left:290px;top:112px;width:62px;height:28px}
  .day-tag--two{left:184px;top:40px;width:28px;height:66px}
  .day-tag--two span{transform:rotate(-90deg);white-space:nowrap}
  .day-disc{position:absolute;width:124px;height:124px;border-radius:50%;background:var(--disc);color:#fff;text-align:center;overflow:hidden;font-size:7px;line-height:1.25;text-transform:uppercase;border:2px solid #fff}
  .day-disc .band{background:var(--blue);font-weight:700;font-size:7.2px;padding:5px 4px;margin-top:22px}
  .day-disc .label{color:var(--blue-light);font-weight:700;margin-top:7px}
  .disc-one{left:270px;top:176px}
  .disc-two{left:180px;top:196px}
  .day-one-copy{position:absolute;left:20px;top:198px;width:238px}
  .day-one-copy .section-title{font-size:12px;margin-bottom:4px}
  .day-one-copy .body-copy{font-size:6.2px}
  .day-two-copy{position:absolute;left:18px;top:36px;width:156px}
  .day-two-copy .section-title{font-size:12.5px;margin-bottom:5px}
  .day-two-copy .body-copy{font-size:5.6px;line-height:1.42}
</style>
</head>
<body>

<!-- Covers: back and front -->
<section class="stage stage--covers">
  <div class="spread">
    <div class="page page--left back-cover">
      <svg class="art" viewBox="0 0 440 340" role="img" aria-label="Coastal photograph with a lighthouse on a rocky shore and three round inset photos of dining and a seaside town">
        <defs>
          <linearGradient id="backSea" x1="0" y1="0" x2="0" y2="1">
            <stop offset="0" stop-color="#dff0fa"/>
            <stop offset=".45" stop-color="#7ec3ea"/>
            <stop offset=".72" stop-color="#2c6fb4"/>
            <stop offset="1" stop-color="#0d2f63"/>
          </linearGradient>
        </defs>
        <path d="M250 0 C215 110 230 210 0 270 L0 340 L440 340 L440 0 Z" fill="url(#backSea)"/>
        <circle cx="300" cy="60" r="42" fill="#8a6a55" stroke="#fff" stroke-width="3"/>
        <circle cx="340" cy="158" r="38" fill="#9fb7c4" stroke="#fff" stroke-width="3"/>
        <circle cx="395" cy="250" r="34" fill="#c9b9a3" stroke="#fff" stroke-width="3"/>
      </svg>
      <div class="contact">
        <h2>CONTACT US</h2>
        <p class="agency">Pinecrest Harbor Guild</p>
        <ul>
          <li><svg viewBox="0 0 10 10"><path d="M5 0a3.5 3.5 0 0 0-3.5 3.5C1.5 6 5 10 5 10s3.5-4 3.5-6.5A3.5 3.5 0 0 0 5 0zm0 5a1.5 1.5 0 1 1 0-3 1.5 1.5 0 0 1 0 3z"/></svg><span>4120 Linden Court,<br>Anchorage, Alaska 56574</span></li>
          <li><svg viewBox="0 0 10 10"><path d="M2 0l2 2.5-1 1.3a6 6 0 0 0 3.2 3.2l1.3-1L10 8 8.3 10C4 9.6.4 6 0 1.7z"/></svg>555-014-2214</li>
          <li><svg viewBox="0 0 10 10"><path d="M2 0l2 2.5-1 1.3a6 6 0 0 0 3.2 3.2l1.3-1L10 8 8.3 10C4 9.6.4 6 0 1.7z"/></svg>555-016-3064</li>
          <li><svg viewBox="0 0 10 10"><path d="M0 2h10v6H0zM0 2l5 3.5L10 2" fill="none" stroke="#1b86d6" stroke-width="1.2"/></svg>info@kelvoro-desk.com</li>
        </ul>
      </div>
      <div class="site back-site">www.kelvoro-desk.com</div>
    </div>
    <div class="page page--right cover">
      <svg class="art" viewBox="0 0 440 340" role="img" aria-label="Aerial photograph of green islands and white yachts on a deep blue Adriatic sea">
        <defs>
          <linearGradient id="coverSea1" x1="0" y1="0" x2="0" y2="1">
            <stop offset="0" stop-color="#d4ecfa"/>
            <stop offset=".25" stop-color="#4aa6e2"/>
            <stop offset=".55" stop-color="#0f5aa8"/>
            <stop offset="1" stop-color="#0a2a55"/>
          </linearGradient>
        </defs>
        <rect width="440" height="340" fill="url(#coverSea1)"/>
      </svg>
      <div class="cover-title">CROATIA</div>
      <div class="cover-tagline">Luxury Explorer<br>Cruise on Dovetail<br>Mini Cruiser</div>
      <div class="cover-dates">23 April - 04 May, 2023<br>08 October - 20 October, 2023</div>
      <div class="site cover-site">www.kelvoro-desk.com</div>
      <div class="cover-credit">By Pinecrest Harbor Guild</div>
    </div>
  </div>
</section>

<!-- Inclusions page and front cover -->
<section class="stage stage--cover-solo">
  <div class="inclusions-page">
    <div class="page">
      <h2 class="section-title">Inclusions &amp; Exclusions</h2>
      <div class="terms">
        <div class="terms-group">
          <h3>Inclusions</h3>
          <ul>
            <li>All transfers per itinerary including airport pick up and drop off</li>
            <li>7 nights cruise on MS Dovetail on half board basis</li>
            <li>All meals stated per itinerary</li>
            <li>Captains dinner</li>
            <li>Unlimited water</li>
            <li>Masseuse on board</li>
            <li>Service of 11 crew members</li>
            <li>Cruise director</li>
            <li>Unlimited WiFi</li>
            <li>Daily cleaning</li>
            <li>Arrival refreshments</li>
            <li>Premium docking</li>
            <li>Usage of non motorized water toys</li>
            <li>Exclusive cocktail reception on Dubrovnik city walls with live music and snacks</li>
          </ul>
        </div>
        <div class="terms-group">
          <h3>Optional Tours</h3>
          <ul>
            <li>Dubrovnik Highlights Explorer tour</li>
            <li>Peljesac Wine tour with live music</li>
            <li>Korcula explorer tour with local estate dinner</li>
            <li>Vis Military tour</li>
            <li>Bortelli Lounge bar reservation (min spend EUR100 per person)</li>
            <li>Split &amp; Trogir ORVALD Explorer tour</li>
            <li>6-course farewell dinner with local wine pairing</li>
            <li>1 night post stay in Velmont 5* hotel in Split (This is added on optional)</li>
          </ul>
        </div>
        <div class="terms-group">
          <h3>Extras</h3>
          <ul>
            <li>Tips for the crew</li>
            <li>Beverage consumption</li>
            <li>Usage of motorized water toys – EUR150 per hour</li>
            <li>International flights</li>
            <li>Any personal expenses</li>
          </ul>
        </div>
      </div>
      <div class="booking">
        <h3>Booking Conditions</h3>
        <p>30 % non-refundable deposit needed upon confirmation.<br>Balance of the trip and any optional tours picked are due 06 May, 2023.</p>
      </div>
      <div class="folio-line"></div>
      <div class="site footer-site on-light">www.kelvoro-desk.com</div>
    </div>
  </div>
  <div class="cover">
    <div class="page">
      <svg class="art" viewBox="0 0 540 418" role="img" aria-label="Aerial photograph of green islands and white yachts on a deep blue Adriatic sea">
        <defs>
          <linearGradient id="coverSea2" x1="0" y1="0" x2="0" y2="1">
            <stop offset="0" stop-color="#d4ecfa"/>
            <stop offset=".25" stop-color="#4aa6e2"/>
            <stop offset=".55" stop-color="#0f5aa8"/>
            <stop offset="1" stop-color="#0a2a55"/>
          </linearGradient>
        </defs>
        <rect width="540" height="418" fill="url(#coverSea2)"/>
      </svg>
      <div class="cover-title">CROATIA</div>
      <div class="cover-tagline">Luxury Explorer<br>Cruise on Dovetail<br>Mini Cruiser</div>
      <div class="cover-dates">23 April - 04 May, 2023<br>08 October - 20 October, 2023</div>
      <div class="site cover-site">www.kelvoro-desk.com</div>
      <div class="cover-credit">By Pinecrest Harbor Guild</div>
    </div>
  </div>
</section>

<!-- Pages 1–2 -->
<section class="stage stage--spread-intro">
  <div class="spread">
    <div class="page page--left">
      <svg class="art" viewBox="0 0 440 340" role="img" aria-label="Photograph of a rocky limestone cliff topped with pine forest above calm sea">
        <defs>
          <linearGradient id="cliff" x1="0" y1="0" x2="0" y2="1">
            <stop offset="0" stop-color="#0d3f86"/>
            <stop offset=".3" stop-color="#2d5f3e"/>
            <stop offset=".55" stop-color="#8a7f76"/>
            <stop offset=".8" stop-color="#4b5a6a"/>
            <stop offset="1" stop-color="#0c2444"/>
          </linearGradient>
        </defs>
        <rect width="440" height="340" fill="url(#cliff)"/>
      </svg>
      <div class="itinerary">
        <h2>Itinerary at a Glance</h2>
        <table>
          <thead>
            <tr><th>Day</th><th>Date</th><th>Program</th></tr>
          </thead>
          <tbody>
            <tr><td class="day">D1</td><td class="date">August 05, 2023</td><td>Arrival to Dubrovnik, Welcome cocktail party on Dubrovnik city walls</td></tr>
            <tr><td class="day">D2</td><td class="date">August 06, 2023</td><td>Dubrovnik Highlights city tour – Embark, sail to Elafiti</td></tr>
            <tr><td class="day">D3</td><td class="date">August 07, 2023</td><td>Sail to Mljet island and day at leisure at sea</td></tr>
            <tr><td class="day">D4</td><td class="date">August 08, 2023</td><td>Peljesac Wine Tasting with Live Music – Sail to Korcula</td></tr>
            <tr><td class="day">D5</td><td class="date">August 09, 2023</td><td>Korcula Highlights Explorer Tour &amp; Local Estate Dinner</td></tr>
            <tr><td class="day">D6</td><td class="date">August 10, 2023</td><td>Korcula to Vis Island sail</td></tr>
            <tr><td class="day">D7</td><td class="date">August 11, 2023</td><td>Vis Military Tour – sail to Pakleni Islands, Bortelli sunset cocktails</td></tr>
            <tr><td class="day">D8</td><td class="date">August 12, 2023</td><td>Hvar island – sail to Split</td></tr>
            <tr><td class="day">D9</td><td class="date">August 13, 2023</td><td>Disembark – Split &amp; Trogir ORVALD tours with 6-course wine dinner</td></tr>
            <tr><td class="day">D10</td><td class="date">August 14, 2023</td><td>Fly out</td></tr>
          </tbody>
        </table>
        <p class="note">Note: All tours &amp; experiences are optional add ons except the cocktail reception on Dubrovnik city walls.</p>
      </div>
      <div class="folio">1</div><div class="folio-line"></div>
      <div class="site footer-site">www.kelvoro-desk.com</div>
    </div>
    <div class="page page--right">
      <svg class="art" viewBox="0 0 440 340" role="img" aria-label="Continuation of the cliff photograph and a round aerial photo of a wooded island with a villa">
        <defs>
          <linearGradient id="cliff2" x1="0" y1="0" x2="0" y2="1">
            <stop offset="0" stop-color="#0d3f86"/>
            <stop offset=".3" stop-color="#2d5f3e"/>
            <stop offset=".55" stop-color="#8a7f76"/>
            <stop offset=".8" stop-color="#4b5a6a"/>
            <stop offset="1" stop-color="#0c2444"/>
          </linearGradient>
          <radialGradient id="islandAerial">
            <stop offset="0" stop-color="#5d7a45"/>
            <stop offset=".7" stop-color="#3e6a4a"/>
            <stop offset="1" stop-color="#1f6d78"/>
          </radialGradient>
        </defs>
        <rect width="440" height="340" fill="url(#cliff2)"/>
        <path d="M178 0 C118 100 126 250 210 340 L440 340 L440 0 Z" fill="#fff"/>
        <path d="M168 0 C140 20 128 40 122 60" fill="none" stroke="#1b86d6" stroke-width="5"/>
        <circle cx="132" cy="165" r="82" fill="url(#islandAerial)" stroke="#fff" stroke-width="3"/>
      </svg>
      <div class="about">
        <h1 class="section-title">About Croatia</h1>
        <p class="body-copy">The Croatian Coast is the premiere setting for the ultimate island hopping experience. The Dalmatian Islands in Croatia are among the most famous in the Mediterranean region. Wild, rugged, and hiding a thousand-year history, many are protected as national park and offer a varied and diverse cruising ground for an yacht charter. The cruising is splendid, encompassing long and short passages to charming anchorages amid rocky islets, ancient villages steeped in history, and translucent waters.</p>
        <p class="body-copy">In total Croatia has over 1200 islands and islets to explore and visit so depending on your travel preference and travel style the combinations of itineraries are endless. Enjoy your cruise on mini cruiser Dovetail by visiting highlights of Adriatic coastline.</p>
      </div>
      <div class="folio">2</div><div class="folio-line"></div>
      <div class="site footer-site">www.kelvoro-desk.com</div>
    </div>
  </div>
</section>

<!-- Pages 3–4 -->
<section class="stage stage--spread-days">
  <div class="spread">
    <div class="page page--left">
      <svg class="art" viewBox="0 0 440 340" role="img" aria-label="Photograph of a stone hut beneath sunlit sandstone cliffs by the sea">
        <defs>
          <linearGradient id="rock" x1="0" y1="0" x2="1" y2="1">
            <stop offset="0" stop-color="#8a6a3e"/>
            <stop offset=".5" stop-color="#b08a58"/>
            <stop offset="1" stop-color="#d7dde2"/>
          </linearGradient>
        </defs>
        <path d="M0 0 L430 0 C380 60 250 140 0 178 Z" fill="url(#rock)"/>
        <path d="M0 178 C250 140 380 60 430 0 L440 0 C400 80 280 165 0 200 Z" fill="#e7e8ea"/>
      </svg>
      <div class="day-tag day-tag--one">DAY 1</div>
      <div class="day-disc disc-one">
        <div class="band">August 5, 2023<br>Arrival to Dubrovnik</div>
        <div class="label">Accommodation</div>
        <div>Mini Cruiser Dovetail</div>
        <div class="label">Meals</div>
        <div>Dinner on board,<br>snack</div>
      </div>
      <div class="day-one-copy">
        <h2 class="section-title">Arrival to Dubrovnik &amp; Welcome Dinner</h2>
        <p class="body-copy">Welcome to Dubrovnik – the pearl of the Adriatic! Dubrovnik lies in the extreme south of Croatia, basking in glorious Mediterranean sunshine for much of the year. A fairytale city of beautiful Baroque, Gothic and Renaissance churches, aristocratic palaces, red-roofed town-houses, magnificent monasteries and fascinating history. Dubrovnik's old town is known as one of the world's finest and most perfectly preserved medieval cities. One of the best views in the world is to be had from its monumental City Walls – be prepared to be amazed!</p>
        <p class="body-copy">Upon arrival, meet your new friends and the crew during welcome reception and dinner on board.</p>
      </div>
      <div class="folio">3</div><div class="folio-line"></div>
      <div class="site footer-site on-light">www.kelvoro-desk.com</div>
    </div>
    <div class="page page--right">
      <svg class="art" viewBox="0 0 440 340" role="img" aria-label="Photograph of guests raising glasses of red wine at a dinner table">
        <defs>
          <linearGradient id="wine" x1="0" y1="0" x2="1" y2="0">
            <stop offset="0" stop-color="#6b5a4a"/>
            <stop offset=".5" stop-color="#3a2a22"/>
            <stop offset="1" stop-color="#5a3a2e"/>
          </linearGradient>
        </defs>
        <path d="M205 0 L440 0 L440 340 L265 340 C205 250 190 110 205 0 Z" fill="url(#wine)"/>
      </svg>
      <div class="day-two-copy">
        <h2 class="section-title">Dubrovnik City Explorer Tour &amp; Wine Event with Live Local Music</h2>
        <p class="body-copy">After breakfast it is the time to Explore the wonders of Dubrovnik's old town, a ORVALD World Heritage Site and one of the most important living historical monuments in this part of Europe. Your local guide will show you this magical medieval town full of legends and give you a glimpse into the incredible history that makes Dubrovnik such a unique city. Explore Dubrovnik's famed City Walls and enjoy a unique view of the Old Town from above, including its narrow streets and small squares. Today Dubrovnik is one of the most beautiful towns in the Mediterranean and you will see why. Dubrovnik used to be an independent republic, surviving mostly on trade. The whole city is alive with tourists and locals who wander the centuries-old streets admiring the architecture. After the city tour, we will have a private wine event in one of the wine cellars within the old town of Dubrovnik. Enjoy local wines accompanied with live music. After the private event, free time in Dubrovnik to enjoy the city on your own before another dinner on board prepared by our chef on board of Dovetail.</p>
      </div>
      <div class="day-tag day-tag--two"><span>DAY 2</span></div>
      <div class="day-disc disc-two">
        <div class="band">August 6, 2023<br>Dubrovnik Walking Tour</div>
        <div class="label">Accommodation</div>
        <div>Mini Cruiser Dovetail</div>
        <div class="label">Meals</div>
        <div>Breakfast on board,<br>dinner on board,<br>snack</div>
      </div>
      <div class="folio">4</div><div class="folio-line"></div>
      <div class="site footer-site on-light">www.kelvoro-desk.com</div>
    </div>
  </div>
</section>

</body>
</html>
```